Business Association Needs Anti-Litter Poster

We are a business association that works to keep our business district clean and safe. We work very hard to keep our streets and parks clean. We are located in a very densely populated part of the city with residents from many parts of the world. We would like a unique poster that that appeals to a multicultural community and reminds residents not to litter. Our community is called City Heights and is located within San Diego, California, USA. Our organizational web site is www.ferngroveba-sample.org

Reason: I extended the deadline in order to provided enough time to get feedback from my committee on which design they like best for the campaign.

```html
<!DOCTYPE html>
<html lang="en">
<head>
<meta charset="utf-8">
<title>Fern Grove Business Association – Anti-Litter Poster</title>
<link href="https://fonts.googleapis.com/css2?family=Comic+Neue:wght@400;700&display=swap" rel="stylesheet">
<style>
  :root {
    --paper: #f1efec;
    --map-tint: #e6e2da;
    --mustard: #e2bd22;
    --steam-brown: #8e5a22;
    --cup-black: #111111;
    --white: #ffffff;
    --orange: #e8891c;
    --gold: #c99a12;
    --crowd-dark: #5a3d28;
    --crowd-mid: #b08662;
    --crowd-light: #e8dccf;
  }
  * { margin: 0; padding: 0; box-sizing: border-box; }
  html, body { width: 849px; height: 1200px; overflow: hidden; background: var(--paper); }
  .poster {
    position: relative;
    width: 849px;
    height: 1200px;
    overflow: hidden;
    font-family: "Comic Neue", "Comic Sans MS", cursive;
    background: var(--paper);
  }
  .area-map {
    position: absolute;
    inset: 0;
    background: radial-gradient(ellipse at 60% 55%, var(--map-tint) 0%, var(--paper) 75%);
  }
  .shapes {
    position: absolute;
    inset: 0;
  }
  .crowd-swirl {
    position: absolute;
    left: 290px;
    top: 285px;
    width: 470px;
    height: 450px;
    border-radius: 50%;
    background: radial-gradient(circle at 50% 52%,
      var(--crowd-dark) 0%, var(--crowd-mid) 30%, #c9a686 52%, var(--crowd-light) 72%, rgba(241,239,236,0) 100%);
    opacity: 0.85;
  }
  .org-name {
    position: absolute;
    top: 48px;
    right: 48px;
    width: 190px;
    text-align: center;
    color: var(--steam-brown);
    font-weight: 700;
    font-size: 26px;
    line-height: 1.1;
  }
  .org-name .mark {
    display: block;
    width: 46px;
    height: 46px;
    margin: 0 auto 12px;
    background: var(--mustard);
  }
  .cup-label {
    position: absolute;
    left: 82px;
    top: 865px;
    color: var(--white);
    font-size: 58px;
    line-height: 1.4;
    font-weight: 400;
  }
  .headline {
    position: absolute;
    left: 300px;
    top: 888px;
    width: 470px;
    text-align: center;
    color: var(--orange);
    font-size: 46px;
    line-height: 1.25;
    font-weight: 400;
  }
  .address {
    position: absolute;
    left: 0;
    right: 0;
    top: 1104px;
    text-align: center;
    color: var(--gold);
    font-size: 18px;
    line-height: 1.65;
    font-weight: 400;
  }
</style>
</head>
<body>
<main class="poster">
  <div class="area-map" role="img" aria-label="Faint street map of the surrounding county"></div>

  <svg class="shapes" width="849" height="1200" viewBox="0 0 849 1200" aria-hidden="true">
    <path class="steam-band" fill="var(--mustard)"
      d="M0,0 H318 C285,60 215,130 225,240 C235,340 250,390 170,480 C95,565 40,640 45,740 L45,1050 L0,1050 Z"/>
    <path class="steam-edge" fill="none" stroke="var(--steam-brown)" stroke-width="10"
      d="M322,0 C290,62 222,132 232,240 C242,342 256,394 176,484 C102,568 48,642 52,735"/>
    <polygon class="cup-lid" fill="var(--cup-black)" points="10,735 302,730 296,768 14,772"/>
    <polygon class="cup-body" fill="var(--cup-black)" points="27,782 268,782 250,1052 45,1052"/>
  </svg>

  <div class="crowd-swirl" role="img" aria-label="Swirl of many smiling community members from diverse backgrounds"></div>

  <div class="org-name"><span class="mark"></span>Fern Grove Business Association</div>

  <p class="cup-label">USE<br>ME</p>

  <h1 class="headline">CLEAN AND SAFE<br>THE WORLD.</h1>

  <p class="address">FERN GROVE BUSINESS ASSOCIATION,1820 MAPLE CREST AVENUE,<br>SUITE 210 LAKEVIEW, CA 90000, 555-014-2290</p>
</main>
</body>
</html>
```